Bright Horizons Circle Charity Launch Day Needs Awesome Promotion

We need promotional leaflets to promote the launch of our new charity. We want to make sure our charity starts with style. We are looking for forward thinking, clever and eye catching design that shows that we are a charity for families and professionals run by parents but that we are a professional organisation. Striking the balance between being bright and family orientated but also keeping us professional. We would like a flyer to hand out to people to advertise the launch day. Our charities mission statement and aims are below. Our strap line is Raising Expectations
We believe that everyone has the right to live their lives to the fullest of their potential. We will work together to raise expectations within the Down's syndrome community and to empower those around us to promote inclusion and achieve aspirations.
With raised expectations and empowered voices, anything is possible.
The above mission statement should be on the leaflet but the additional details below are not necessary but included to give you more information about us. If you feel it adds to the design then you can use the information.
Aims
Raising expectations of
•	The public. By educating the community and showing them how much people with Down’s syndrome can achieve we can raise expectations and change attitudes. We want to help build a community in which people with DS are not merely accepted and catered for but one in which they make meaningful positive contributions to the community. Often the community wants to help but needs the information and support to empower them to do so.
•	The parents and carers. The day of diagnosis, that moment when we stop being the public and become the parent. Many parents will never have encountered people with Down’s syndrome in their lives before, they won’t know what to expect and we want to help support, inform and train those parents to understand what their children may be able to achieve. To see past the diagnosis and to unlock the potential in their loved one.
•	The person with Down’s syndrome. If no one around us expects us to do well then the chances are we won’t. We want to empower those people caring for a person with Down’s syndrome to have high expectations and in turn pass those high expectations on to those they care for. To drive aspiration and empower people with Down’s syndrome to have high expectations of themselves.
•	Professionals. Many professionals do not have specific training in enabling a person with Down’s syndrome. We aim to raise the expectations of the professionals working with people with Down’s syndrome and their families. If they are empowered with the knowledge and skills to truly unlock potential and drive aspiration then they can go on to help so many families. Seeing that person as part of a network, part of a community, part of a family can empower people to not just treat impairments but to drive change and promote inclusion.
What we do.
•	Training. We are going to provide a range of training aimed at both parents and professionals. The training will cover many areas including but not restricted to SEN law, education, therapies, social/behaviour approaches, independent living, transition to adulthood.
•	Education and awareness. We are working with Marlowe Hollins University to run education sessions with undergraduate midwives, we are now moving on to participate with a collaborative module between all health and social care students. We will be presenting about our experiences of person centred working and team work. We hope to build on this and help provide awareness training in many settings from acute hospitals to voluntary organisations like scouting.
•	Information. Our goal is to provide pertinent information on our website and link to other useful sources. This is a work in progress and we will look to build upon this as we go. We hope to provide local advice so that each family can use the experience of the community to find the best resources and build a database of all useful local information.
•	Support. Potentially the most important aim of our charity. At every step our families need support; we aim to provide support to the families and carers so they can continue to support the person with Down’s syndrome to live life to the fullest of their potential.
Our launch day is a launch reception with refreshments, information and entertainment. It includes a family sponsored walk that is accessible to all including wheelchairs users and young children.
It is being held at
Felbrook Hollow Woods Country Park
Gravesend
Kent
TN27 8QP
on Sunday 22nd May 2016
It will start at 11.00am with refreshments and walk at 12.30pm.
Contact details are
www.brighthorizonscircle.org.uk
info@brighthorizonscircle.org.uk
We would like people to email to register for the walk and go to the website for details. The website will be up soon but is currently under construction but has our logo etc on it for you to see. I have attached copies of logo and strap line. We would like to use these colours in the design and particularly picking out the blue.
Our charity number is 1093748 and must be included. We also need the phrase 'working in partnership with Garden County Family Link group but we would like this to be very small and not prominent please.
I have attached some promotional photos we have as well our logo and other information.

Updates
Just a note, the main aim of the leaflet is to sell the launch day. All the additional info about the charity was for you to understand where we are coming from. The short mission statement should be in their but not necessarily the aims and what we do bits. Include what you think really sells the launch and the sponsored walk ( including need to register). Thanks Looking forward to some awesome designs. Added Monday, March 14, 2016
Target Market(s)
families, education, health and social care professionals.
Industry/Entity Type
Charity
Requirements
Must have
- Logo
- Mission statement
- info about sponsored walk and guidance to register for this. People must register
- Date, time venue of launch day
- webpage
- charity number
- Working in partnership with Garden County Family Link Group. Phrase must be included but it needs to be small and inconspicuous.

Nice to have
- Some photo images of the children.

Should not have
- To much writing. It needs to be clear and concise

```html
<!DOCTYPE html>
<html lang="en">
<head>
<meta charset="utf-8">
<title>Bright Horizons Circle – Leaflet</title>
<link href="https://fonts.googleapis.com/css2?family=Arimo:wght@400;700&family=Tinos:wght@700&display=swap" rel="stylesheet">
<style>
  :root{
    --navy:#2a3a8c;
    --magenta:#e5137f;
    --blue:#1ea9e6;
    --green:#9bc83c;
    --yellow:#fff100;
    --ink:#1b1b1b;
    --white:#ffffff;
    --backdrop:#e9e6e1;
  }
  *{box-sizing:border-box;margin:0;padding:0}
  html,body{width:1200px;height:800px;overflow:hidden}
  body{background:var(--backdrop);font-family:"Arimo",Arial,sans-serif;position:relative}

  .leaflet-page{position:absolute;top:46px;width:500px;height:708px;background:var(--magenta);overflow:hidden;box-shadow:0 6px 18px rgba(0,0,0,.25)}
  .page-front{left:75px}
  .page-back{left:625px}

  /* front: header */
  .top-stripe{position:absolute;left:0;top:0;width:100%;height:16px;background:var(--navy)}
  .photo-grid{position:absolute;left:0;top:16px;width:100%;height:222px;background:var(--magenta)}
  .photo{position:absolute}
  .photo-ballpit{left:6px;top:52px;width:170px;height:94px;background:linear-gradient(135deg,#e8432f,#2f8fd8 55%,#f2c21b)}
  .photo-playtime{left:6px;top:150px;width:170px;height:68px;background:linear-gradient(135deg,#c9b9a8,#7d6a9a)}
  .photo-reading{left:180px;top:66px;width:150px;height:80px;background:linear-gradient(135deg,#f1ede6,#5a5f7a)}
  .photo-group{left:180px;top:150px;width:150px;height:68px;background:linear-gradient(135deg,#e7dcc9,#a8a099)}
  .photo-book{left:334px;top:0;width:160px;height:96px;background:linear-gradient(135deg,#d8cdb8,#3f8a5a)}
  .photo-crafts{left:334px;top:100px;width:160px;height:118px;background:linear-gradient(135deg,#eae3d6,#c05a74)}
  .logo-tab{position:absolute;left:110px;top:0;width:216px;height:62px;background:var(--yellow);border-radius:0 0 60px 0;display:flex;align-items:center;gap:8px;padding-left:16px}
  .logo-mark{width:22px;height:22px;border-radius:50%;background:var(--navy);flex:none}
  .logo-name{font-weight:700;font-size:17px;color:var(--navy);line-height:1.05}

  .mission{position:absolute;left:0;top:238px;width:100%;height:130px;background:var(--yellow);padding:14px 22px 0;font-family:"Tinos","Times New Roman",serif;font-weight:700;font-size:13.6px;line-height:1.32;color:var(--ink);text-align:justify}
  .mission p+p{margin-top:12px}

  .section-tab{position:absolute;height:34px;display:flex;align-items:center;justify-content:center}
  .section-tab svg{position:absolute;inset:0}
  .section-tab h2{position:relative;font-size:15px;font-weight:700;color:var(--ink);padding-left:24px}

  .aim-box{position:absolute;left:0;width:100%;padding:10px 20px 0 20px;color:var(--white);font-size:10.6px;line-height:1.38;text-align:justify}
  .aim-box p{padding-left:14px;text-indent:-14px}
  .box-blue{background:var(--blue)}
  .box-green{background:var(--green)}

  /* back */
  .services{position:absolute;left:0;width:100%;padding:0 22px;color:var(--white);font-size:10px;line-height:1.36;text-align:justify}
  .services p{padding-left:12px;text-indent:-12px;margin-bottom:12px}
  .services strong{font-weight:700}
  .call-to-action{position:absolute;left:0;bottom:0;width:100%;height:104px;background:var(--blue);padding:12px 22px;color:var(--navy);font-weight:700;font-size:10px;line-height:1.4;text-align:justify}
</style>
</head>
<body>

<section class="leaflet-page page-front">
  <div class="top-stripe"></div>
  <div class="photo-grid">
    <div class="photo photo-ballpit" role="img" aria-label="Photo of a smiling child playing in a colourful ball pit"></div>
    <div class="photo photo-playtime" role="img" aria-label="Photo of two children playing together at a table"></div>
    <div class="photo photo-reading" role="img" aria-label="Photo of a parent and child sharing an activity"></div>
    <div class="photo photo-group" role="img" aria-label="Photo of a group of children sitting together"></div>
    <div class="photo photo-book" role="img" aria-label="Photo of a young person holding a book"></div>
    <div class="photo photo-crafts" role="img" aria-label="Photo of children doing crafts at a table"></div>
    <div class="logo-tab">
      <span class="logo-mark"></span>
      <span class="logo-name">Bright Horizons Circle</span>
    </div>
  </div>

  <div class="mission">
    <p>We believe that everyone has the right to live their lives to the fullest of their potential. We will work together to raise expectations within the Down's syndrome community and to empower those around us to promote inclusion and achieve aspirations.</p>
    <p>With raised expectations and empowered voices, anything is possible.</p>
  </div>

  <div class="section-tab" style="left:60px;top:380px;width:400px">
    <svg width="400" height="34" viewBox="0 0 400 34" aria-hidden="true"><polygon points="0,0 400,0 400,30 24,30 0,34" fill="#fff"/><polygon points="0,0 24,30 0,34" fill="#cfcfcf"/></svg>
    <h2>Raising expectations of</h2>
  </div>

  <div class="aim-box box-blue" style="top:418px;height:124px">
    <p>•&nbsp;&nbsp; The public. By educating the community and showing them how much people with Down’s syndrome can achieve we can raise expectations and change attitudes. We want to help build a community in which people with DS are not merely accepted and catered for but one in which they make meaningful positive contributions to the community. Often the community wants to help but needs the information and support to empower them to do so.</p>
  </div>

  <div class="aim-box box-green" style="top:556px;height:124px">
    <p>•&nbsp;&nbsp; The parents and carers. The day of diagnosis, that moment when we stop being the public and become the parent. Many parents will never have encountered people with Down’s syndrome in their lives before, they won’t know what to expect and we want to help support, inform and train those parents to understand what their children may be able to achieve. To see past the diagnosis and to unlock the potential in their loved one.</p>
  </div>
</section>

<section class="leaflet-page page-back">
  <div class="aim-box box-blue" style="top:12px;height:118px">
    <p>•&nbsp;&nbsp; The person with Down’s syndrome. If no one around us expects us to do well then the chances are we won’t. We want to empower those people caring for a person with Down’s syndrome to have high expectations and in turn pass those high expectations on to those they care for. To drive aspiration and empower people with Down’s syndrome to have high expectations of themselves.</p>
  </div>

  <div class="aim-box box-green" style="top:142px;height:132px">
    <p>•&nbsp;&nbsp; Professionals. Many professionals do not have specific training in enabling a person with Down’s syndrome. We aim to raise the expectations of the professionals working with people with Down’s syndrome and their families. If they are empowered with the knowledge and skills to truly unlock potential and drive aspiration then they can go on to help so many families. Seeing that person as part of a network, part of a community, part of a family can empower people to not just treat impairments but to drive change and promote inclusion.</p>
  </div>

  <div class="section-tab" style="left:110px;top:288px;width:340px">
    <svg width="340" height="34" viewBox="0 0 340 34" aria-hidden="true"><polygon points="0,0 340,0 340,30 24,30 0,34" fill="#fff"/><polygon points="0,0 24,30 0,34" fill="#cfcfcf"/></svg>
    <h2>What we do</h2>
  </div>

  <div class="services" style="top:336px">
    <p>• <strong>Training:</strong> We are going to provide a range of training aimed at both parents and professionals. The training will cover many areas including but not restricted to SEN law, education, therapies, social/behaviour approaches, independent living, transition to adulthood.</p>
    <p>• <strong>Education and awareness:</strong> We are working with Marlowe Hollins University to run education sessions with undergraduate midwives, we are now moving on to participate with a collaborative module between all health and social care students. We will be presenting about our experiences of person centred working and team work. We hope to build on this and help provide awareness training in many settings from acute hospitals to voluntary organisations like scouting.</p>
    <p>• <strong>Information:</strong> Our goal is to provide pertinent information on our website and link to other useful sources. This is a work in progress and we will look to build upon this as we go. We hope to provide local advice so that each family can use the experience of the community to find the best resources and build a database of all useful local information.</p>
    <p>• <strong>Support:</strong> Potentially the most important aim of our charity. At every step our families need support; we aim to provide support to the families and carers so they can continue to support the person with Down’s syndrome to live life to the fullest of their potential.</p>
  </div>

  <div class="call-to-action">
    Would your business be able to support us? We are a local, dynamic and driven team who are determined to make an impact in our community. Could you be a part of it? Could you sponsor a specific event or help us with advertising, venues or catering? Is your business looking for a charity to support? If so then please contact us at info@brighthorizonscircle.org.uk or just get in touch to chat with one of the team.
  </div>
</section>

</body>
</html>
```